Gently Harbor BC 2019

Hi!
As seen from the attached, I created a 2018 BC that I really like.
It features company details on one side, and a calendar on the other side. The BC is 7" x 2" with a score, so folded it's a regular sized BC.
Company details remain the same, but I need to upgrade and refresh the calendar to 2019. Let your creative juices flow!

The submitted designs so far, while not terrible, most don't take into account that I need a refresher on the current design, but it's a BC that is double sided, and the size of a BC that's side by side wide, with score. (see the attached BC 2018 design). I need the BC to be updated with a 2019 calendar, but essentially because it's such a tiny size, to work the realistic space allocated, and make it readable and striking to stand out and very usable/practical. Let's do this people!

```html
<!DOCTYPE html>
<html lang="en">
<head>
<meta charset="utf-8">
<title>Gently Harbor – 2019 Calendar Business Card</title>
<link href="https://fonts.googleapis.com/css2?family=Caveat:wght@400;500&family=Courier+Prime:wght@400;700&family=Montserrat:wght@200;600;700&family=Roboto:wght@400&display=swap" rel="stylesheet">
<style>
  :root{
    --page:#362e2e;
    --paper:#ffffff;
    --ink:#000000;
    --band:#231f20;
    --cyan:#20abe2;
    --magenta:#ec008c;
    --yellow:#fff200;
    --teal:#13a086;
    --sunday:#e8283a;
    --rule:#231f20;
  }
  *{margin:0;padding:0;box-sizing:border-box}
  html,body{width:1200px;height:1200px;overflow:hidden;background:var(--page)}
  .canvas{position:relative;width:1200px;height:1200px}

  /* ---------- front side ---------- */
  .card-front{position:absolute;left:92px;top:98px;width:998px;height:326px;background:var(--paper)}
  .slogans{position:absolute;left:96px;top:70px;width:325px}
  .slogan{display:block;width:325px;height:26px;border-radius:13px;margin-bottom:13px;white-space:nowrap;overflow:hidden;
    font:400 15px/26px "Courier Prime",monospace;letter-spacing:1.2px;padding-left:20px;color:var(--ink)}
  .slogan--cyan{background:var(--cyan)}
  .slogan--magenta{background:var(--magenta)}
  .slogan--yellow{background:var(--yellow)}
  .brand{position:absolute;left:640px;top:134px;display:flex;align-items:center;gap:10px;white-space:nowrap}
  .brand-mark{width:22px;height:22px;background:var(--magenta)}
  .brand-name{font:400 28px/1 "Courier Prime",monospace;color:var(--ink)}

  .contact-band{position:absolute;left:0;top:214px;width:998px;height:112px;background:var(--ink);color:#fff}
  .motto{position:absolute;left:68px;top:30px;font:400 35px/1.2 "Caveat",cursive;letter-spacing:.5px;white-space:nowrap}
  .contact-row{position:absolute;left:534px;width:414px;display:flex;justify-content:space-between;align-items:center;white-space:nowrap}
  .contact-row--phones{top:14px;padding-bottom:8px;border-bottom:2px solid #fff}
  .contact-row--web{top:56px}
  .contact-item{display:flex;align-items:center;gap:7px;font:400 13px/1 "Roboto",sans-serif}
  .contact-row--web .contact-item{font:400 13.5px/1 "Courier Prime",monospace}
  .contact-item svg{width:16px;height:16px;fill:none;stroke:#fff;stroke-width:1.8}
  .contact-item svg.solid{fill:#fff;stroke:none}

  /* ---------- calendar side ---------- */
  .card-back{position:absolute;left:92px;top:578px;width:998px;height:326px;background:var(--paper)}
  .calendar-head{height:60px;background:var(--band);color:#fff;position:relative}
  .calendar-theme{position:absolute;left:54px;top:26px;font:400 23px/1 "Caveat",cursive}
  .calendar-year{position:absolute;right:50px;top:16px;font:200 36px/1 "Montserrat",sans-serif;color:#e8e8e8}
  .month{position:absolute;width:143px;font-family:"Montserrat",sans-serif}
  .month h3{text-align:center;font:700 11px/1 "Montserrat",sans-serif;letter-spacing:.8px;color:var(--teal);height:18px}
  .weekdays,.days{display:grid;grid-template-columns:repeat(7,1fr);list-style:none;text-align:center}
  .weekdays{font:600 7.5px/1 "Montserrat",sans-serif;padding-bottom:5px;border-bottom:1px solid var(--rule);margin-bottom:4px}
  .weekdays li:first-child{color:var(--sunday)}
  .days{font:700 7.5px/12.8px "Montserrat",sans-serif;color:var(--ink)}
  .days li:first-child{grid-column-start:var(--start)}
  .days .su{color:var(--sunday)}
</style>
</head>
<body>
<div class="canvas">

  <section class="card-front">
    <div class="slogans">
      <span class="slogan slogan--cyan">Fill your toner with purpose</span>
      <span class="slogan slogan--magenta">Fill your planet with hope</span>
      <span class="slogan slogan--yellow">Fill your world with kindness</span>
    </div>
    <div class="brand">
      <span class="brand-mark"></span>
      <span class="brand-name">Gently Harbor</span>
    </div>

    <div class="contact-band">
      <p class="motto">We do good stuff with your stuff</p>
      <div class="contact-row contact-row--phones">
        <span class="contact-item">
          <svg class="solid" viewBox="0 0 24 24"><path d="M6.6 10.8a15 15 0 0 0 6.6 6.6l2.2-2.2c.3-.3.7-.4 1-.2 1.1.4 2.3.6 3.6.6.6 0 1 .4 1 1V20c0 .6-.4 1-1 1A17 17 0 0 1 3 4c0-.6.4-1 1-1h3.5c.6 0 1 .4 1 1 0 1.3.2 2.5.6 3.6.1.3 0 .7-.2 1z"/></svg>
          555.201.4470</span>
        <span class="contact-item">
          <svg class="solid" viewBox="0 0 24 24"><path d="M3 4h13a2 2 0 0 1 2 2v6a2 2 0 0 1-2 2H8l-4 4v-4H3a2 2 0 0 1-2-2V6a2 2 0 0 1 2-2zm17 4h1a2 2 0 0 1 2 2v6a2 2 0 0 1-2 2h-1v3l-3-3h-6a2 2 0 0 1-2-2h7a3 3 0 0 0 3-3z"/></svg>
          555.201.4481</span>
        <span class="contact-item">
          <svg viewBox="0 0 24 24"><rect x="3" y="8" width="18" height="13" rx="1"/><path d="M7 8V3h8l2 2v3M7 12h2M11 12h2M15 12h2M7 16h2M11 16h2M15 16h2"/></svg>
          555.201.4472</span>
      </div>
      <div class="contact-row contact-row--web">
        <span class="contact-item">
          <svg viewBox="0 0 24 24"><rect x="2" y="5" width="20" height="14" rx="1"/><path d="M2 6l10 7 10-7"/></svg>
          pickup@gentlyharbor.com</span>
        <span class="contact-item">
          <svg viewBox="0 0 24 24"><rect x="4" y="5" width="16" height="11"/><path d="M1 19h22"/></svg>
          gentlyharbor.com</span>
      </div>
    </div>
  </section>

  <section class="card-back">
    <header class="calendar-head">
      <p class="calendar-theme">Fill Your Day with Purpose</p>
      <p class="calendar-year">2019</p>
    </header>

    <div class="month" style="left:18px;top:78px"><h3>JANUARY</h3>
      <ol class="weekdays"><li>S</li><li>M</li><li>T</li><li>W</li><li>T</li><li>F</li><li>S</li></ol>
      <ol class="days" style="--start:3"><li>1</li><li>2</li><li>3</li><li>4</li><li>5</li><li class="su">6</li><li>7</li><li>8</li><li>9</li><li>10</li><li>11</li><li>12</li><li class="su">13</li><li>14</li><li>15</li><li>16</li><li>17</li><li>18</li><li>19</li><li class="su">20</li><li>21</li><li>22</li><li>23</li><li>24</li><li>25</li><li>26</li><li class="su">27</li><li>28</li><li>29</li><li>30</li><li>31</li></ol></div>

    <div class="month" style="left:180px;top:78px"><h3>FEBRUARY</h3>
      <ol class="weekdays"><li>S</li><li>M</li><li>T</li><li>W</li><li>T</li><li>F</li><li>S</li></ol>
      <ol class="days" style="--start:6"><li>1</li><li>2</li><li class="su">3</li><li>4</li><li>5</li><li>6</li><li>7</li><li>8</li><li>9</li><li class="su">10</li><li>11</li><li>12</li><li>13</li><li>14</li><li>15</li><li>16</li><li class="su">17</li><li>18</li><li>19</li><li>20</li><li>21</li><li>22</li><li>23</li><li class="su">24</li><li>25</li><li>26</li><li>27</li><li>28</li></ol></div>

    <div class="month" style="left:342px;top:78px"><h3>MARCH</h3>
      <ol class="weekdays"><li>S</li><li>M</li><li>T</li><li>W</li><li>T</li><li>F</li><li>S</li></ol>
      <ol class="days" style="--start:6"><li>1</li><li>2</li><li class="su">3</li><li>4</li><li>5</li><li>6</li><li>7</li><li>8</li><li>9</li><li class="su">10</li><li>11</li><li>12</li><li>13</li><li>14</li><li>15</li><li>16</li><li class="su">17</li><li>18</li><li>19</li><li>20</li><li>21</li><li>22</li><li>23</li><li class="su">24</li><li>25</li><li>26</li><li>27</li><li>28</li><li>29</li><li>30</li><li class="su">31</li></ol></div>

    <div class="month" style="left:504px;top:78px"><h3>APRIL</h3>
      <ol class="weekdays"><li>S</li><li>M</li><li>T</li><li>W</li><li>T</li><li>F</li><li>S</li></ol>
      <ol class="days" style="--start:2"><li>1</li><li>2</li><li>3</li><li>4</li><li>5</li><li>6</li><li class="su">7</li><li>8</li><li>9</li><li>10</li><li>11</li><li>12</li><li>13</li><li class="su">14</li><li>15</li><li>16</li><li>17</li><li>18</li><li>19</li><li>20</li><li class="su">21</li><li>22</li><li>23</li><li>24</li><li>25</li><li>26</li><li>27</li><li class="su">28</li><li>29</li><li>30</li></ol></div>

    <div class="month" style="left:666px;top:78px"><h3>MAY</h3>
      <ol class="weekdays"><li>S</li><li>M</li><li>T</li><li>W</li><li>T</li><li>F</li><li>S</li></ol>
      <ol class="days" style="--start:4"><li>1</li><li>2</li><li>3</li><li>4</li><li class="su">5</li><li>6</li><li>7</li><li>8</li><li>9</li><li>10</li><li>11</li><li class="su">12</li><li>13</li><li>14</li><li>15</li><li>16</li><li>17</li><li>18</li><li class="su">19</li><li>20</li><li>21</li><li>22</li><li>23</li><li>24</li><li>25</li><li class="su">26</li><li>27</li><li>28</li><li>29</li><li>30</li><li>31</li></ol></div>

    <div class="month" style="left:828px;top:78px"><h3>JUNE</h3>
      <ol class="weekdays"><li>S</li><li>M</li><li>T</li><li>W</li><li>T</li><li>F</li><li>S</li></ol>
      <ol class="days" style="--start:7"><li>1</li><li class="su">2</li><li>3</li><li>4</li><li>5</li><li>6</li><li>7</li><li>8</li><li class="su">9</li><li>10</li><li>11</li><li>12</li><li>13</li><li>14</li><li>15</li><li class="su">16</li><li>17</li><li>18</li><li>19</li><li>20</li><li>21</li><li>22</li><li class="su">23</li><li>24</li><li>25</li><li>26</li><li>27</li><li>28</li><li>29</li><li class="su">30</li></ol></div>

    <div class="month" style="left:18px;top:205px"><h3>JULY</h3>
      <ol class="weekdays"><li>S</li><li>M</li><li>T</li><li>W</li><li>T</li><li>F</li><li>S</li></ol>
      <ol class="days" style="--start:2"><li>1</li><li>2</li><li>3</li><li>4</li><li>5</li><li>6</li><li class="su">7</li><li>8</li><li>9</li><li>10</li><li>11</li><li>12</li><li>13</li><li class="su">14</li><li>15</li><li>16</li><li>17</li><li>18</li><li>19</li><li>20</li><li class="su">21</li><li>22</li><li>23</li><li>24</li><li>25</li><li>26</li><li>27</li><li class="su">28</li><li>29</li><li>30</li><li>31</li></ol></div>

    <div class="month" style="left:180px;top:205px"><h3>AUGUST</h3>
      <ol class="weekdays"><li>S</li><li>M</li><li>T</li><li>W</li><li>T</li><li>F</li><li>S</li></ol>
      <ol class="days" style="--start:5"><li>1</li><li>2</li><li>3</li><li class="su">4</li><li>5</li><li>6</li><li>7</li><li>8</li><li>9</li><li>10</li><li class="su">11</li><li>12</li><li>13</li><li>14</li><li>15</li><li>16</li><li>17</li><li class="su">18</li><li>19</li><li>20</li><li>21</li><li>22</li><li>23</li><li>24</li><li class="su">25</li><li>26</li><li>27</li><li>28</li><li>29</li><li>30</li><li>31</li></ol></div>

    <div class="month" style="left:342px;top:205px"><h3>SEPTEMBER</h3>
      <ol class="weekdays"><li>S</li><li>M</li><li>T</li><li>W</li><li>T</li><li>F</li><li>S</li></ol>
      <ol class="days" style="--start:1"><li class="su">1</li><li>2</li><li>3</li><li>4</li><li>5</li><li>6</li><li>7</li><li class="su">8</li><li>9</li><li>10</li><li>11</li><li>12</li><li>13</li><li>14</li><li class="su">15</li><li>16</li><li>17</li><li>18</li><li>19</li><li>20</li><li>21</li><li class="su">22</li><li>23</li><li>24</li><li>25</li><li>26</li><li>27</li><li>28</li><li class="su">29</li><li>30</li></ol></div>

    <div class="month" style="left:504px;top:205px"><h3>OCTOBER</h3>
      <ol class="weekdays"><li>S</li><li>M</li><li>T</li><li>W</li><li>T</li><li>F</li><li>S</li></ol>
      <ol class="days" style="--start:3"><li>1</li><li>2</li><li>3</li><li>4</li><li>5</li><li class="su">6</li><li>7</li><li>8</li><li>9</li><li>10</li><li>11</li><li>12</li><li class="su">13</li><li>14</li><li>15</li><li>16</li><li>17</li><li>18</li><li>19</li><li class="su">20</li><li>21</li><li>22</li><li>23</li><li>24</li><li>25</li><li>26</li><li class="su">27</li><li>28</li><li>29</li><li>30</li><li>31</li></ol></div>

    <div class="month" style="left:666px;top:205px"><h3>NOVEMBER</h3>
      <ol class="weekdays"><li>S</li><li>M</li><li>T</li><li>W</li><li>T</li><li>F</li><li>S</li></ol>
      <ol class="days" style="--start:6"><li>1</li><li>2</li><li class="su">3</li><li>4</li><li>5</li><li>6</li><li>7</li><li>8</li><li>9</li><li class="su">10</li><li>11</li><li>12</li><li>13</li><li>14</li><li>15</li><li>16</li><li class="su">17</li><li>18</li><li>19</li><li>20</li><li>21</li><li>22</li><li>23</li><li class="su">24</li><li>25</li><li>26</li><li>27</li><li>28</li><li>29</li><li>30</li></ol></div>

    <div class="month" style="left:828px;top:205px"><h3>DECEMBER</h3>
      <ol class="weekdays"><li>S</li><li>M</li><li>T</li><li>W</li><li>T</li><li>F</li><li>S</li></ol>
      <ol class="days" style="--start:1"><li class="su">1</li><li>2</li><li>3</li><li>4</li><li>5</li><li>6</li><li>7</li><li class="su">8</li><li>9</li><li>10</li><li>11</li><li>12</li><li>13</li><li>14</li><li class="su">15</li><li>16</li><li>17</li><li>18</li><li>19</li><li>20</li><li>21</li><li class="su">22</li><li>23</li><li>24</li><li>25</li><li>26</li><li>27</li><li>28</li><li class="su">29</li><li>30</li><li>31</li></ol></div>
  </section>

</div>
</body>
</html>
```